Eco friendly Swedish beauty products sold in aluminum bottles - label design needed

We need help in designing a series of stick on labels for 80 ml (2.7 fl. oz.) aluminum bottles containing beauty products such as soaps, shampoo etc. The diameter of the bottle is 36 mm and the body of the bottles measures approx. 106 mm.
It is important for us that the label has a simplistic and clean feel with few colors (and the right ones!) and that the label helps amplify this product being both better and a more sustainable alternative to many of our plastic bottle competitors. The design and label should communicate the feel of an Eco-friendly, sustainable and modern brand of high quality - and with a Swedish concept.
We are using Montserrat font in our materials. Find attached information of preferred colors, the bottles and one example of our logotype. I am also available on e-mail should further information be needed.

Looking forward and very excited to receive your suggestions.
Note that we are expecting to start selling a series of approximately 10 different products where I will need one "master design" and then only smaller changes for each of the different products.

Target Market(s)

People whom are aware and not only look at price tag. Private and commercial market.

Industry/Entity Type

Beauty

Font styles to use
Other font styles liked:
• Montserrat

Requirements
Must have
• It must give the feel of being both better and a more sustainable alternative to many of our plastic bottle competitors.
Nice to have
• Simplistic. Clean. Clear.
Should not have
• Wrong colors, too complex designs.

```html
<!DOCTYPE html>
<html lang="en">
<head>
<meta charset="utf-8">
<title>Norrvik – Hand Sanitizer Label</title>
<link href="https://fonts.googleapis.com/css2?family=Bebas+Neue&family=Montserrat:wght@400;500&display=swap" rel="stylesheet">
<style>
  :root {
    --page: #ffffff;
    --label: #e4e1dc;
    --label-light: #ebe9e5;
    --rust: #7a2412;
    --rust-soft: #a45a44;
    --ink-white: #f4ede9;
  }
  * { margin: 0; padding: 0; box-sizing: border-box; }
  html, body {
    width: 1200px; height: 1200px; overflow: hidden;
    background: var(--page);
  }
  .canvas { position: relative; width: 1200px; height: 1200px; }
  .label {
    position: absolute; left: 332px; top: 94px;
    width: 536px; height: 1012px;
    background: linear-gradient(90deg, var(--label-light) 0%, var(--label) 55%, #d9d5cf 100%);
    font-family: "Montserrat", sans-serif;
    color: var(--rust);
  }
  .rule-thick {
    position: absolute; left: 0; width: 100%; height: 12px;
    background: linear-gradient(90deg, var(--rust) 0%, var(--rust-soft) 50%, var(--rust) 100%);
  }
  .rule-thick.top { top: 25px; }
  .rule-thick.bottom { top: 981px; }
  .brand {
    position: absolute; top: 136px; left: 0; width: 100%;
    text-align: center;
    font-weight: 500; font-size: 54px; letter-spacing: 1px;
    color: var(--rust-soft);
    line-height: 1;
  }
  .product-name {
    position: absolute; top: 326px; left: 0; width: 100%;
    text-align: center;
    font-family: "Bebas Neue", sans-serif;
    font-weight: 400;
    font-size: 104px; line-height: 98px;
    color: var(--rust);
  }
  .product-name span { display: block; }
  .product-name .second { color: var(--rust-soft); }
  .icon-plus {
    position: absolute; top: 548px; left: 50%; transform: translateX(-50%);
    width: 100px; height: 100px;
  }
  .claim {
    position: absolute; top: 672px; left: 0; width: 100%;
    text-align: center;
    font-weight: 500; font-size: 25px; letter-spacing: 3px;
    color: var(--rust);
  }
  .thin-rule {
    position: absolute; left: 46px; width: 444px; height: 2px;
    background: var(--rust-soft);
  }
  .thin-rule.upper { top: 734px; }
  .thin-rule.lower { top: 812px; }
  .badge {
    position: absolute; top: 744px; left: 34px; width: 486px; height: 56px;
    background: linear-gradient(90deg, var(--rust) 0%, var(--rust-soft) 50%, var(--rust) 100%);
    color: var(--ink-white);
    font-weight: 400; font-size: 28px; letter-spacing: 3px;
    display: flex; align-items: center; justify-content: center;
  }
  .dots {
    position: absolute; top: 878px; left: 50%; transform: translateX(-50%);
    display: flex; gap: 5px;
  }
  .dots i { width: 7px; height: 7px; border-radius: 50%; background: var(--rust); display: block; }
  .volume {
    position: absolute; top: 924px; left: 0; width: 100%;
    text-align: center;
    font-weight: 400; font-size: 32px; letter-spacing: 1px;
    color: var(--rust);
  }
</style>
</head>
<body>
<main class="canvas">
  <section class="label">
    <div class="rule-thick top"></div>

    <div class="brand">Norrvik</div>

    <h1 class="product-name">
      <span>HAND</span>
      <span class="second">SANITIZER</span>
    </h1>

    <svg class="icon-plus" viewBox="0 0 100 100" aria-hidden="true">
      <circle cx="50" cy="50" r="46" fill="none" stroke="#a45a44" stroke-width="3"/>
      <circle cx="48" cy="48" r="36" fill="#7a2412"/>
      <rect x="45" y="30" width="6" height="36" rx="2" fill="#f4ede9"/>
      <rect x="30" y="45" width="36" height="6" rx="2" fill="#f4ede9"/>
    </svg>

    <p class="claim">·NATURAL INGREDIENTS·</p>

    <div class="thin-rule upper"></div>
    <div class="badge">KILL 99.9 % OF GERMS</div>
    <div class="thin-rule lower"></div>

    <div class="dots"><i></i><i></i><i></i></div>
    <p class="volume">200ml</p>

    <div class="rule-thick bottom"></div>
  </section>
</main>
</body>
</html>
```